The Lantern and Harbor: for Rosalind and Elias by Dorsey Valtane

I need an album cover design for a song dedicated to Elias and Rosalind Hale Barrow, in anticipation for EHB weekend. the main question the song raises is: when was the last time someone said that you can achieve greatness? In other words, we often do not live to our full potential. The design should be simple and clean, using a modern Sans Serif font. 1600 x 1600 pixels, best-quality RGB mode, and delivered as a JPEG.

Target Market(s)

young men and women, 18-35 years old

Font styles to use
Sans Serif

Colors
3277b5
34a7d7

Requirements
Must have
• Name of song (The Lantern and Harbor: for Rosalind and Elias) and artist (Dorsey Valtane)
Nice to have
• Something suggesting elegance without being overt or pretentious
Should not have
• Serif font, too many colors

```html
<!DOCTYPE html>
<html lang="en">
<head>
<meta charset="UTF-8">
<title>The Lantern and Harbor: for Rosalind and Elias — Dorsey Valtane</title>
<link rel="stylesheet" href="https://fonts.googleapis.com/css2?family=Jost:wght@300;400;600;700&display=swap">
<style>
  :root {
    --ink: #0b0d10;
    --sky-night: #1c355f;
    --sky-deep: #2f5f8e;
    --sky-teal: #6cc9c8;
    --sky-aqua: #45e3d3;
    --sky-mint: #9ff0e2;
    --cloud-cream: #f4eedd;
    --crown-tone: rgba(11, 13, 16, 0.82);
  }

  * { margin: 0; padding: 0; box-sizing: border-box; }

  html, body {
    width: 1200px;
    height: 1200px;
    overflow: hidden;
    background: var(--sky-teal);
  }

  .cover {
    position: relative;
    width: 1200px;
    height: 1200px;
    overflow: hidden;
    font-family: "Jost", "Futura", sans-serif;
    color: var(--ink);
  }

  .sky-backdrop {
    position: absolute;
    inset: 0;
    background:
      radial-gradient(ellipse 520px 420px at 1000px 420px, rgba(244, 238, 221, 0.95), rgba(244, 238, 221, 0) 70%),
      radial-gradient(ellipse 420px 360px at 820px 820px, rgba(244, 238, 221, 0.7), rgba(244, 238, 221, 0) 70%),
      radial-gradient(ellipse 700px 520px at 120px 80px, var(--sky-night), rgba(28, 53, 95, 0) 75%),
      radial-gradient(ellipse 600px 400px at 150px 1050px, var(--sky-aqua), rgba(69, 227, 211, 0) 75%),
      linear-gradient(170deg, var(--sky-deep) 0%, var(--sky-teal) 38%, var(--sky-mint) 62%, var(--sky-aqua) 100%);
  }

  .crown-mark {
    position: absolute;
    left: 515px;
    top: 256px;
    width: 166px;
    height: 134px;
    border-radius: 50% 50% 12px 12px / 60% 60% 12px 12px;
    background: var(--crown-tone);
  }

  .song-title {
    position: absolute;
    left: 0;
    right: 0;
    top: 432px;
    text-align: center;
    font-weight: 600;
    font-size: 128px;
    line-height: 130px;
    letter-spacing: 0.01em;
    text-transform: uppercase;
  }

  .song-title .title-line { display: block; }

  .dedication {
    position: absolute;
    left: 0;
    right: 0;
    top: 758px;
    text-align: center;
    font-weight: 600;
    font-size: 52px;
    line-height: 60px;
    letter-spacing: -0.005em;
    text-transform: uppercase;
  }

  .artist-name {
    position: absolute;
    left: 0;
    right: 0;
    top: 1078px;
    text-align: center;
    font-weight: 400;
    font-size: 26px;
    line-height: 34px;
    letter-spacing: 0.22em;
    text-transform: uppercase;
  }
</style>
</head>
<body>
  <main class="cover">
    <div class="sky-backdrop" role="img" aria-label="Photograph of a starry teal and navy sky with soft cream clouds and a flock of birds in flight"></div>

    <div class="crown-mark" role="img" aria-label="Small black silhouette of an ornate crown"></div>

    <h1 class="song-title">
      <span class="title-line">The Lantern</span>
      <span class="title-line">and Harbor:</span>
    </h1>

    <p class="dedication">For Rosalind and Elias</p>

    <p class="artist-name">Dorsey Valtane</p>
  </main>
</body>
</html>
```